Brom-leigh Sky Harbour Custom Brokers Limited

Shop online from the USA and Ship to Jamaica
Customs Brokerage, Import Export and logistic Services
Address:- 238-240 Halden Brook Road Kingston Jamaica
Email: info@bromleighskyharbour,com
Web: www.bromleighskyharbour.com
Telephone: (876) 555-0148, (876) 555-0193
flyer should be quarter page must print information on back and front

```html
<!DOCTYPE html>
<html lang="en">
<head>
<meta charset="utf-8">
<title>Bromleigh Sky Harbour Custom Brokers – Quarter Page Flyer</title>
<link href="https://fonts.googleapis.com/css2?family=Catamaran:wght@400;500;700;800&family=Montserrat:wght@500;600&display=swap" rel="stylesheet">
<style>
:root{
  --navy:#13294b;
  --gold:#e9ab22;
  --ink:#3a3a3a;
  --grey:#5b5b5b;
  --soft:#7a7a7a;
  --page:#ececec;
  --white:#ffffff;
}
*{box-sizing:border-box;margin:0;padding:0}
html,body{width:1200px;height:2169px;overflow:hidden;background:var(--page)}
body{position:relative;font-family:"Catamaran",sans-serif;color:var(--ink)}
.flyer{position:absolute;left:62px;width:1075px;height:695px;background:var(--white);overflow:hidden;box-shadow:0 18px 40px rgba(0,0,0,.18)}
.flyer--front{top:250px}
.flyer--back{top:1230px}
.flyer__art{position:absolute;inset:0;width:1075px;height:695px}

.brand{position:absolute;text-align:right}
.brand__name{display:block;font-weight:700;font-size:24px;color:var(--navy);line-height:1;white-space:nowrap}
.brand__sub{display:block;font-weight:400;font-size:16px;color:var(--soft);margin-top:6px;line-height:1;white-space:nowrap}
.flyer--front .brand{right:38px;top:118px}
.flyer--back .brand{right:45px;top:96px}
.flyer--back .brand__name{color:var(--white)}
.flyer--back .brand__sub{color:var(--white)}

.headline{position:absolute;right:38px;top:222px;text-align:right;font-size:45px;line-height:47px;color:var(--navy);font-weight:500;letter-spacing:-.5px}
.headline strong{font-weight:800}
.headline .accent{color:var(--gold);font-weight:700}
.services-line{position:absolute;right:38px;top:440px;text-align:right;font-size:35px;line-height:46px;color:var(--grey);font-weight:400}
.gold-tab{position:absolute;right:0;top:462px;width:17px;height:116px;background:var(--gold)}

.contact{position:absolute;display:flex;align-items:center;gap:8px;font-size:22px;color:var(--navy);white-space:nowrap}
.contact svg{flex:none}
.contact__gap{width:10px}
.flyer--front .contact{right:38px;top:604px}
.flyer--back .contact{left:55px;top:604px}
.band{position:absolute;left:0;right:0;bottom:0;height:47px;background:var(--navy)}
.band__info{position:absolute;display:flex;align-items:center;gap:12px;font-size:22px;color:var(--white);white-space:nowrap;top:9px}
.flyer--front .band__info{right:38px}
.flyer--back .band__info{left:55px}

.section-title{position:absolute;left:55px;font-family:"Montserrat",sans-serif;font-weight:600;font-size:27px;color:var(--navy);letter-spacing:.3px}
.section-title span{color:var(--gold)}
.section-title::after{content:"";position:absolute;left:2px;bottom:-12px;width:34px;height:3px;background:var(--navy)}
.about-title{top:44px}
.services-title{top:232px}
.about-text{position:absolute;left:53px;top:92px;width:455px;font-size:15.5px;line-height:19px;color:var(--grey)}

.service{position:absolute;display:flex;gap:16px;align-items:flex-start}
.service__icon{width:54px;height:54px;border-radius:50%;display:flex;align-items:center;justify-content:center;flex:none}
.service__icon--gold{background:var(--gold)}
.service__icon--navy{background:var(--navy)}
.service__name{font-family:"Montserrat",sans-serif;font-weight:600;font-size:14px;color:var(--navy);margin-top:4px;letter-spacing:.2px}
.service__desc{font-size:14px;line-height:18px;color:var(--grey);margin-top:4px;white-space:nowrap}
.service--shipping{left:55px;top:310px}
.service--imports{left:310px;top:310px}
.service--logistics{left:55px;top:406px}
.service--export{left:310px;top:406px}
.service--customs{left:55px;top:498px}
</style>
</head>
<body>

<section class="flyer flyer--front">
  <svg class="flyer__art" viewBox="0 0 1075 695">
    <defs>
      <linearGradient id="sky" x1="0" y1="0" x2="0.6" y2="1">
        <stop offset="0" stop-color="#6f7f8c"/>
        <stop offset=".45" stop-color="#c9a57a"/>
        <stop offset="1" stop-color="#8a5a3e"/>
      </linearGradient>
      <linearGradient id="handover" x1="0" y1="0" x2="1" y2="1">
        <stop offset="0" stop-color="#d9e3ea"/>
        <stop offset=".5" stop-color="#d9a865"/>
        <stop offset="1" stop-color="#2f5fa0"/>
      </linearGradient>
    </defs>
    <path d="M500,0 H620 C740,70 740,260 680,400 C600,560 380,640 0,690 V605 C210,585 470,545 590,430 C680,330 680,110 500,0 Z" fill="var(--gold)"/>
    <g role="img" aria-label="Cargo plane taking off over stacked shipping containers at sunset">
      <path d="M0,0 H520 C610,50 640,160 630,290 C615,430 520,510 370,555 C230,585 100,598 0,608 Z" fill="url(#sky)"/>
    </g>
    <path d="M535,0 C660,70 680,240 620,370" fill="none" stroke="var(--navy)" stroke-width="6"/>
    <path d="M0,640 C190,612 340,585 475,520" fill="none" stroke="var(--navy)" stroke-width="6"/>
    <rect x="180" y="648" width="895" height="47" fill="var(--navy)"/>
    <path d="M0,695 V655 C120,640 230,630 330,612 C280,640 220,665 185,695 Z" fill="var(--gold)"/>
    <circle cx="482" cy="388" r="190" fill="var(--gold)"/>
    <circle cx="482" cy="388" r="184" fill="var(--navy)"/>
    <g role="img" aria-label="Courier handing a cardboard parcel to a customer">
      <circle cx="482" cy="388" r="177" fill="url(#handover)"/>
    </g>
  </svg>

  <div class="brand">
    <span class="brand__name">BROMLEIGH SKY HARBOUR</span>
    <span class="brand__sub">Custom Brokers Limited</span>
  </div>

  <h1 class="headline"><strong>SHOP ONLINE</strong><br>FROM THE <span class="accent">USA</span><br>AND SHIP TO<br><span class="accent">JAMAICA</span></h1>
  <p class="services-line">Customs Brokerage,<br>Import Export and<br>logistic Services</p>
  <div class="gold-tab"></div>

  <div class="contact">
    <svg width="20" height="22" viewBox="0 0 20 22"><path d="M6,2 C3,3 2,7 4,11 C6,16 10,20 14,20 C16,20 17,18 17,17 L14,14 L11,16 C9,14 7,11 7,9 L9,7 Z" fill="none" stroke="var(--gold)" stroke-width="1.8" stroke-linejoin="round"/></svg>
    <span>(876) 555-0148, (876) 555-0193</span><span class="contact__gap"></span>
    <svg width="24" height="22" viewBox="0 0 24 22"><path d="M2,10 L22,2 L15,20 L11,13 Z M11,13 L22,2" fill="none" stroke="var(--gold)" stroke-width="1.8" stroke-linejoin="round"/></svg>
    <span>info@bromleighskyharbour.com</span>
  </div>
  <div class="band">
    <div class="band__info">
      <svg width="18" height="24" viewBox="0 0 18 24"><path d="M9,22 C4,15 2,11 2,8 A7,7 0 0 1 16,8 C16,11 14,15 9,22 Z" fill="none" stroke="var(--gold)" stroke-width="1.8"/><circle cx="9" cy="8" r="2.6" fill="none" stroke="var(--gold)" stroke-width="1.6"/></svg>
      <span>238-240 Halden Brook Road Kingston Jamaica</span><span class="contact__gap"></span>
      <svg width="22" height="22" viewBox="0 0 22 22"><g fill="none" stroke="var(--gold)" stroke-width="1.6"><circle cx="11" cy="11" r="9"/><ellipse cx="11" cy="11" rx="4" ry="9"/><path d="M2,11 H20 M3.5,6.5 H18.5 M3.5,15.5 H18.5"/></g></svg>
      <span>www.bromleighskyharbour.com</span>
    </div>
  </div>
</section>

<section class="flyer flyer--back">
  <svg class="flyer__art" viewBox="0 0 1075 695">
    <defs>
      <linearGradient id="harbour" x1="0" y1="0" x2="0.4" y2="1">
        <stop offset="0" stop-color="#e9b48c"/>
        <stop offset=".5" stop-color="#b9705c"/>
        <stop offset="1" stop-color="#3f3a48"/>
      </linearGradient>
      <linearGradient id="cartons" x1="0" y1="0" x2="0" y2="1">
        <stop offset="0" stop-color="#d9b27c"/>
        <stop offset="1" stop-color="#b48650"/>
      </linearGradient>
    </defs>
    <path d="M700,0 H1075 V695 H1060 C820,570 560,400 565,215 C570,115 620,40 690,0 Z" fill="var(--gold)"/>
    <g role="img" aria-label="Container ship loaded with cargo sailing at sunset">
      <path d="M775,0 H1075 V615 C880,545 690,395 668,230 C655,125 700,45 775,0 Z" fill="url(#harbour)"/>
    </g>
    <path d="M735,0 C655,55 620,160 628,255 C645,420 800,560 1010,695" fill="none" stroke="var(--navy)" stroke-width="5"/>
    <g role="img" aria-label="Stack of cardboard shipping cartons from online stores">
      <path d="M612,385 H745 V440 H805 V596 H545 V445 H612 Z" fill="url(#cartons)"/>
    </g>
    <rect x="0" y="648" width="1075" height="47" fill="var(--navy)"/>
  </svg>

  <h2 class="section-title about-title">ABOUT <span>US</span></h2>
  <p class="about-text">Sed ut perspiciatis unde omnis iste natus error sit voluptatem accusantium dol orem que laudantium, totam rem aperiam, eaque ipsa quae ab illo invent ore veritatis et quasi architecto beatae vitae dicta sunt explicabo. Nemo enim ipsam voluptatem quia volupt as sit aspernatur aut odit aut fugit, sed quia consequunt ur magni dolores eos qui ratione voluptatem sequi nesciunt.Neque</p>

  <h2 class="section-title services-title">OUR <span>SERVICES</span></h2>

  <div class="service service--shipping">
    <div class="service__icon service__icon--gold"><svg width="30" height="26" viewBox="0 0 30 26"><g fill="none" stroke="#fff" stroke-width="1.6"><rect x="2" y="4" width="16" height="14"/><path d="M18,9 H24 L28,14 V18 H18"/><circle cx="8" cy="20" r="2.5"/><circle cx="23" cy="20" r="2.5"/></g></svg></div>
    <div><div class="service__name">SHIPPING</div><div class="service__desc">Sed ut perspiciatis unde<br>omnis iste natus error</div></div>
  </div>
  <div class="service service--imports">
    <div class="service__icon service__icon--gold"><svg width="30" height="30" viewBox="0 0 30 30"><g fill="none" stroke="#fff" stroke-width="1.6"><circle cx="15" cy="15" r="7"/><ellipse cx="15" cy="15" rx="3" ry="7"/><path d="M8,15 H22 M3,3 L8,8 M27,3 L22,8 M3,27 L8,22 M27,27 L22,22"/></g></svg></div>
    <div><div class="service__name">IMPORTS</div><div class="service__desc">Sed ut perspiciatis unde<br>omnis iste natus error</div></div>
  </div>
  <div class="service service--logistics">
    <div class="service__icon service__icon--navy"><svg width="30" height="26" viewBox="0 0 30 26"><g fill="none" stroke="#fff" stroke-width="1.6"><path d="M3,20 V8 H11 L14,14 V20 Z M17,2 V20 H28"/><rect x="20" y="10" width="7" height="7"/><circle cx="7" cy="21" r="2.5"/></g></svg></div>
    <div><div class="service__name">LOGISTICS</div><div class="service__desc">Sed ut perspiciatis unde<br>iste natus error</div></div>
  </div>
  <div class="service service--export">
    <div class="service__icon service__icon--navy"><svg width="28" height="26" viewBox="0 0 28 26"><g fill="none" stroke="#fff" stroke-width="1.6" stroke-linejoin="round"><path d="M20,4 H4 V22 H22 V14"/><path d="M10,16 C11,10 16,8 22,8 M18,4 L22,8 L18,12"/></g></svg></div>
    <div><div class="service__name">EXPORT</div><div class="service__desc">Sed ut perspiciatis unde<br>omnis iste natus error</div></div>
  </div>
  <div class="service service--customs">
    <div class="service__icon service__icon--gold"><svg width="28" height="30" viewBox="0 0 28 30"><g fill="none" stroke="#fff" stroke-width="1.6"><rect x="3" y="3" width="13" height="16"/><rect x="11" y="10" width="13" height="17"/><path d="M14,19 L17,22 L22,15"/></g></svg></div>
    <div><div class="service__name">CUSTOMS CLEARANCE</div><div class="service__desc">Sed ut perspiciatis unde omnis iste natus error</div></div>
  </div>

  <div class="brand">
    <span class="brand__name">BROMLEIGH SKY HARBOUR</span>
    <span class="brand__sub">Custom Brokers Limited</span>
  </div>

  <div class="contact">
    <svg width="20" height="22" viewBox="0 0 20 22"><path d="M6,2 C3,3 2,7 4,11 C6,16 10,20 14,20 C16,20 17,18 17,17 L14,14 L11,16 C9,14 7,11 7,9 L9,7 Z" fill="none" stroke="var(--gold)" stroke-width="1.8" stroke-linejoin="round"/></svg>
    <span>(876) 555-0148, (876) 555-0193</span><span class="contact__gap"></span>
    <svg width="24" height="22" viewBox="0 0 24 22"><path d="M2,10 L22,2 L15,20 L11,13 Z M11,13 L22,2" fill="none" stroke="var(--gold)" stroke-width="1.8" stroke-linejoin="round"/></svg>
    <span>info@bromleighskyharbour.com</span>
  </div>
  <div class="band">
    <div class="band__info">
      <svg width="18" height="24" viewBox="0 0 18 24"><path d="M9,22 C4,15 2,11 2,8 A7,7 0 0 1 16,8 C16,11 14,15 9,22 Z" fill="none" stroke="var(--gold)" stroke-width="1.8"/><circle cx="9" cy="8" r="2.6" fill="none" stroke="var(--gold)" stroke-width="1.6"/></svg>
      <span>238-240 Halden Brook Road Kingston Jamaica</span><span class="contact__gap"></span>
      <svg width="22" height="22" viewBox="0 0 22 22"><g fill="none" stroke="var(--gold)" stroke-width="1.6"><circle cx="11" cy="11" r="9"/><ellipse cx="11" cy="11" rx="4" ry="9"/><path d="M2,11 H20 M3.5,6.5 H18.5 M3.5,15.5 H18.5"/></g></svg>
      <span>www.bromleighskyharbour.com</span>
    </div>
  </div>
</section>

</body>
</html>
```